Trucking Insurance Website Design

We are working with a Trucking Insurance company in California. They provide vehicle insurance for trucking companies and truckers.
As you might imagine, there are no websites we could find for inspiration for trucking insurance. But below are sites that do similar insurance.
https://pinemeadowcover.com/trucking-insurance/
https://www.haulsafeplan.com/california-commercial-truck-insurance
Thank you for taking the time to consider designing a website for us. We are web developers based in Stockton, CA, USA. Most of our projects go through the same process. Understanding this process may help you win a project with us. We custom-code all of our websites in-house. We don’t have any requirements as to what tools you use for your design, but we ask that you follow these guidelines.
IMAGES:
If you use any images or icons in the design, we ask that you have a link to the asset so we can purchase the image/icon. Most of the designs we submit do not have the customer’s images on them unless they have some great images. Be creative; show us the feeling you are trying to portray with your image choices. Use any royalty-free site you choose. We subscribe to Quillon and mainly use their images, but we can purchase images outside of Quillon. PLEASE NOTE: we will not submit designs to clients with watermarks on the images.
FONTS:
We ask that you identify the fonts you’re using in the design. This can be done in a message if you want. We typically use Tavlo Fonts and Quillon Fonts.
CONTENT:
We're always open to different content and ideas. We often submit designs with stock images so the client can see our vision. We typically take pictures after the website launch to use their images with our vision. Lorem Ipsum is fine for paragraphs, but we ask that you make the Headers with correct English. We want to be able to show the vision and identify the sections of the website.
INSPIRATION:
We typically add a couple of links in the brief of websites we like to help you get started in your design.
REVISIONS:
We do not often ask for revisions of the designs unless we see something in the design that may not appeal to the client. If there are slight changes that we want to make, we do that in the development process.
FEEDBACK:
We rarely give feedback on designs during the design process. We are working on many website projects and do not have the time to provide feedback. We usually respond if your request is well thought out and asks specific questions, but a note asking “feedback, please” usually goes unanswered.
1 page

```html
<!DOCTYPE html>
<html lang="en">
<head>
<meta charset="utf-8">
<title>Roadline Cover — Trucking Insurance</title>
<link href="https://fonts.googleapis.com/css2?family=Montserrat:wght@400;600;700;800&family=Open+Sans:wght@400;600&display=swap" rel="stylesheet">
<style>
:root{
  --blue:#4257c9;
  --blue-dark:#2e3f9e;
  --red:#d2302c;
  --navy:#1d2335;
  --navy-2:#272d42;
  --ink:#2b2f3a;
  --muted:#6c7080;
  --light:#ececef;
  --gray:#dcdce0;
  --footer:#1f232b;
  --footer-bar:#16191f;
  --white:#ffffff;
}
*{margin:0;padding:0;box-sizing:border-box}
html,body{width:678px;height:1200px;overflow:hidden}
body{font-family:"Open Sans",Arial,sans-serif;color:var(--ink);background:var(--white);position:relative}
h1,h2,h3,h4,.nav,.btn,.tag{font-family:"Montserrat",Arial,sans-serif}

/* header */
.site-header{position:absolute;top:0;left:0;width:678px;height:44px;background:var(--white)}
.logo{position:absolute;left:24px;top:11px;display:flex;align-items:center;gap:6px;font-family:"Montserrat",sans-serif;font-weight:700;font-size:10px;color:var(--blue-dark);letter-spacing:.5px}
.logo i{width:18px;height:18px;border-radius:50%;background:var(--blue-dark);display:block}
.topbar{position:absolute;right:0;top:0;width:360px;height:13px;background:var(--navy);color:#cfd3e6;font-size:6px;display:flex;justify-content:flex-end;align-items:center;gap:12px;padding-right:22px}
.topbar b{color:var(--white);font-weight:600}
.nav{position:absolute;right:0;top:13px;width:360px;height:31px;background:var(--blue);display:flex;align-items:center;justify-content:flex-end;gap:18px;padding-right:22px;font-size:6.5px;font-weight:700;color:var(--white);letter-spacing:.4px}
.nav svg{width:10px;height:10px}

/* hero */
.hero{position:absolute;top:44px;left:0;width:678px;height:256px;background:linear-gradient(180deg,#aebccd 0%,#7f90a6 45%,#4a5463 75%,#2c313b 100%)}
.hero-text{position:absolute;left:64px;top:62px;color:var(--white)}
.hero-text .rule{width:60px;height:3px;background:var(--red);margin-bottom:7px}
.hero-text h1{font-size:23px;font-weight:800;line-height:1.02;letter-spacing:.3px}
.hero-text p{font-size:10px;font-style:italic;margin-top:3px;opacity:.95}
.btn{position:absolute;left:64px;top:134px;background:var(--red);color:var(--white);font-size:6.5px;font-weight:700;padding:6px 10px;letter-spacing:.5px;display:flex;align-items:center;gap:5px}

/* user cards band */
.band{position:absolute;top:300px;left:0;width:678px;height:253px;background:var(--navy);background-image:repeating-linear-gradient(45deg,rgba(255,255,255,.025) 0 2px,transparent 2px 6px)}
.cards{position:absolute;top:268px;left:33px;display:flex;gap:33px}
.card{width:182px;height:228px;background:var(--white);box-shadow:0 3px 10px rgba(0,0,0,.25)}
.card .photo{height:96px;position:relative}
.card .tag{position:absolute;right:0;bottom:0;background:var(--red);color:var(--white);font-size:5.5px;font-weight:700;padding:3px 6px;letter-spacing:.4px}
.card .body{padding:9px 9px 0;border-top:3px solid var(--red)}
.card h3{font-size:8px;font-weight:700;color:var(--ink);margin-bottom:5px}
.card p{font-size:5.6px;line-height:1.55;color:var(--muted)}

/* services */
.offer{position:absolute;top:553px;left:0;width:678px;height:240px;background:var(--light)}
.offer h2{text-align:center;margin-top:27px;font-size:13px;font-weight:800;color:var(--blue)}
.offer .sub{text-align:center;font-size:6px;color:var(--muted);margin-top:2px}
.grid{position:absolute;left:30px;top:68px;width:618px;display:grid;grid-template-columns:repeat(6,1fr);row-gap:18px}
.svc{text-align:center;padding:0 6px}
.svc svg{width:18px;height:18px;display:block;margin:0 auto 6px}
.svc h4{font-size:6px;font-weight:700;color:var(--ink);margin-bottom:4px}
.svc p{font-size:5.2px;line-height:1.5;color:var(--muted)}

/* news / clients / agent */
.lower{position:absolute;top:793px;left:0;width:678px;height:212px;background:var(--gray);border-top:18px solid #e6e6ea}
.col-title{font-family:"Montserrat",sans-serif;font-size:7px;font-weight:700;color:var(--ink);margin-bottom:10px;letter-spacing:.3px}
.news{position:absolute;left:30px;top:14px;width:190px}
.news-item{display:flex;gap:8px;margin-bottom:12px}
.news-item .thumb{width:58px;height:46px;flex:none}
.news-item .date{display:inline-block;background:var(--white);font-size:5.5px;padding:2px 5px;color:var(--muted);margin-bottom:3px}
.news-item h4{font-size:6.5px;font-weight:700;line-height:1.3}
.news-item p{font-size:5.2px;color:var(--muted);line-height:1.4}
.news-item .more{font-size:5.5px;color:var(--blue);font-weight:600;margin-top:3px}
.clients{position:absolute;left:236px;top:0;width:205px;height:194px;background:var(--navy-2);color:#d6d9e6;padding:14px 16px}
.clients .col-title{color:var(--white)}
.clients blockquote{font-size:5.8px;line-height:1.6;font-style:italic}
.clients .who{margin-top:10px;font-family:"Montserrat",sans-serif;font-size:6px;font-weight:700;color:var(--white)}
.clients .who span{display:block;font-weight:400;color:#a8adc2;font-size:5.3px;margin-top:2px}
.clients .arrows{position:absolute;bottom:14px;right:16px;display:flex;gap:4px}
.clients .arrows svg{width:12px;height:12px}
.agent{position:absolute;left:458px;top:14px;width:190px}
.agent .portrait{width:66px;height:66px;border-radius:50%;margin-bottom:8px}
.agent p{font-size:5.6px;color:var(--muted);line-height:1.5}
.agent .phone{margin-top:6px;font-family:"Montserrat",sans-serif;font-size:8px;font-weight:700;color:var(--blue);display:flex;align-items:center;gap:4px}

/* footer */
.site-footer{position:absolute;top:1005px;left:0;width:678px;height:175px;background:var(--footer);color:#b9bdc9;padding:20px 30px;display:grid;grid-template-columns:1fr 1fr 1fr 1fr;gap:22px}
.site-footer h4{font-size:7px;font-weight:700;color:var(--white);margin-bottom:4px;letter-spacing:.3px}
.site-footer .line{width:22px;height:2px;background:var(--blue);margin-bottom:9px}
.site-footer ul{list-style:none;font-size:5.6px;line-height:2}
.site-footer ul li::before{content:"› ";color:var(--blue)}
.site-footer p{font-size:5.6px;line-height:1.6;margin-bottom:6px}
.field{display:flex;margin-top:6px}
.field span{flex:1;height:14px;background:#2d323c;font-size:5px;padding:4px 5px;color:#7e8494}
.field b{width:18px;height:14px;background:var(--blue);display:flex;align-items:center;justify-content:center}
.footer-bar{position:absolute;top:1180px;left:0;width:678px;height:20px;background:var(--footer-bar);color:#8b909d;font-size:5.5px;text-align:center;line-height:20px}
</style>
</head>
<body>

<header class="site-header">
  <div class="logo"><i></i>ROADLINE COVER</div>
  <div class="topbar"><b>1-888-000-0000</b><span>Log in</span></div>
  <nav class="nav">
    <span>HOME</span><span>ABOUT US</span><span>SERVICES</span><span>NEWS</span><span>FAQ</span>
    <svg viewBox="0 0 12 12" fill="none" stroke="#fff" stroke-width="1.6"><circle cx="5" cy="5" r="3.6"/><path d="M7.7 7.7l3 3"/></svg>
  </nav>
</header>

<section class="hero" role="img" aria-label="Photo of a semi truck driving on an open highway under a pale sky">
  <div class="hero-text">
    <div class="rule"></div>
    <h1>OWNER SLOGAN<br>GOES HERE</h1>
    <p>Other motto can go here!</p>
  </div>
  <div class="btn">REQUEST A QUOTE <svg width="6" height="6" viewBox="0 0 6 6"><path d="M1 1l3 2-3 2" fill="none" stroke="#fff" stroke-width="1.2"/></svg></div>
</section>

<div class="band"></div>
<div class="cards">
  <article class="card">
    <div class="photo" role="img" aria-label="Photo of a truck driver leaning on his truck" style="background:linear-gradient(135deg,#8a6c54,#c9b49d 55%,#5d5046)"><span class="tag">READ MORE</span></div>
    <div class="body"><h3>USER TYPE 1</h3><p>Lorem ipsum dolor sit amet, consectetur adipiscing elit, sed do eiusmod tempor incididunt ut labore et dolore magna aliqua. Ut enim ad minim veniam, quis nostrud exercitation ullamco laboris nisi ut aliquip ex ea commodo consequat duis aute.</p></div>
  </article>
  <article class="card">
    <div class="photo" role="img" aria-label="Photo of a smiling driver in a truck cab" style="background:linear-gradient(135deg,#6f6a63,#b8aa96 55%,#4a4440)"><span class="tag">READ MORE</span></div>
    <div class="body"><h3>USER TYPE 2</h3><p>Lorem ipsum dolor sit amet, consectetur adipiscing elit, sed do eiusmod tempor incididunt ut labore et dolore magna aliqua. Ut enim ad minim veniam, quis nostrud exercitation ullamco laboris nisi ut aliquip ex ea commodo consequat duis aute.</p></div>
  </article>
  <article class="card">
    <div class="photo" role="img" aria-label="Photo of a fleet manager standing beside trucks" style="background:linear-gradient(135deg,#7b8797,#c4ccd6 55%,#3f4856)"><span class="tag">READ MORE</span></div>
    <div class="body"><h3>USER TYPE 3</h3><p>Lorem ipsum dolor sit amet, consectetur adipiscing elit, sed do eiusmod tempor incididunt ut labore et dolore magna aliqua. Ut enim ad minim veniam, quis nostrud exercitation ullamco laboris nisi ut aliquip ex ea commodo consequat duis aute.</p></div>
  </article>
</div>

<section class="offer">
  <h2>WHAT WE OFFER</h2>
  <p class="sub">Trusted trucking insurance services</p>
  <div class="grid">
    <div class="svc"><svg viewBox="0 0 20 20" fill="none" stroke="#4257c9" stroke-width="1.4"><path d="M10 2l6 2.5v5c0 4-2.7 6.7-6 8.5-3.3-1.8-6-4.5-6-8.5v-5z"/></svg><h4>SERVICE LIST 1</h4><p>Short description for service list 1 lorem ipsum dolor sit amet.</p></div>
    <div class="svc"><svg viewBox="0 0 20 20" fill="none" stroke="#4257c9" stroke-width="1.4"><rect x="4" y="3" width="12" height="15" rx="1"/><path d="M7 7h6M7 10h6M7 13h4"/></svg><h4>SERVICE LIST 2</h4><p>Short description for service list 2 lorem ipsum dolor sit amet.</p></div>
    <div class="svc"><svg viewBox="0 0 20 20" fill="none" stroke="#4257c9" stroke-width="1.4"><circle cx="10" cy="10" r="7.5"/><path d="M6.5 10.2l2.4 2.4 4.6-4.8"/></svg><h4>SERVICE LIST 3</h4><p>Short description for service list 3 lorem ipsum dolor sit amet.</p></div>
    <div class="svc"><svg viewBox="0 0 20 20" fill="none" stroke="#4257c9" stroke-width="1.4"><path d="M10 18s-5.5-5.3-5.5-9.5a5.5 5.5 0 0111 0C15.5 12.7 10 18 10 18z"/><circle cx="10" cy="8.5" r="2"/></svg><h4>SERVICE LIST 4</h4><p>Short description for service list 4 lorem ipsum dolor sit amet.</p></div>
    <div class="svc"><svg viewBox="0 0 20 20" fill="none" stroke="#4257c9" stroke-width="1.4"><rect x="2" y="6" width="11" height="8"/><path d="M13 9h3l2 2.5V14h-5"/><circle cx="6" cy="15" r="1.6"/><circle cx="15" cy="15" r="1.6"/></svg><h4>SERVICE LIST 5</h4><p>Short description for service list 5 lorem ipsum dolor sit amet.</p></div>
    <div class="svc"><svg viewBox="0 0 20 20" fill="none" stroke="#4257c9" stroke-width="1.4"><rect x="3" y="4" width="14" height="12" rx="1"/><path d="M3 8h14M7 12h6"/></svg><h4>SERVICE LIST 6</h4><p>Short description for service list 6 lorem ipsum dolor sit amet.</p></div>
    <div class="svc"><svg viewBox="0 0 20 20" fill="none" stroke="#4257c9" stroke-width="1.4"><rect x="4" y="3" width="12" height="15" rx="1"/><path d="M7 7h6M7 10h6M7 13h4"/></svg><h4>SERVICE LIST 7</h4><p>Short description for service list 7 lorem ipsum dolor sit amet.</p></div>
    <div class="svc"><svg viewBox="0 0 20 20" fill="none" stroke="#4257c9" stroke-width="1.4"><path d="M10 2l6 2.5v5c0 4-2.7 6.7-6 8.5-3.3-1.8-6-4.5-6-8.5v-5z"/><path d="M7.3 10l2 2 3.5-3.7"/></svg><h4>SERVICE LIST 8</h4><p>Short description for service list 8 lorem ipsum dolor sit amet.</p></div>
    <div class="svc"><svg viewBox="0 0 20 20" fill="none" stroke="#4257c9" stroke-width="1.4"><circle cx="10" cy="10" r="7.5"/><path d="M10 5.5V10l3 2"/></svg><h4>SERVICE LIST 9</h4><p>Short description for service list 9 lorem ipsum dolor sit amet.</p></div>
    <div class="svc"><svg viewBox="0 0 20 20" fill="none" stroke="#4257c9" stroke-width="1.4"><path d="M5 3h3l1.5 4-2 1.3a9 9 0 004.2 4.2l1.3-2 4 1.5v3a1.5 1.5 0 01-1.6 1.5A14 14 0 013.5 4.6 1.5 1.5 0 015 3z"/></svg><h4>SERVICE LIST 10</h4><p>Short description for service list 10 lorem ipsum dolor sit amet.</p></div>
    <div class="svc"><svg viewBox="0 0 20 20" fill="none" stroke="#4257c9" stroke-width="1.4"><path d="M10 18s-5.5-5.3-5.5-9.5a5.5 5.5 0 0111 0C15.5 12.7 10 18 10 18z"/><circle cx="10" cy="8.5" r="2"/></svg><h4>SERVICE LIST 11</h4><p>Short description for service list 11 lorem ipsum dolor sit amet.</p></div>
    <div class="svc"><svg viewBox="0 0 20 20" fill="none" stroke="#4257c9" stroke-width="1.4"><path d="M10 2l6 2.5v5c0 4-2.7 6.7-6 8.5-3.3-1.8-6-4.5-6-8.5v-5z"/></svg><h4>SERVICE LIST 12</h4><p>Short description for service list 12 lorem ipsum dolor sit amet.</p></div>
  </div>
</section>

<section class="lower">
  <div class="news">
    <h3 class="col-title">COMPANY NEWS</h3>
    <div class="news-item">
      <div class="thumb" role="img" aria-label="Photo of trucks parked at a depot" style="background:linear-gradient(135deg,#3d8a9a,#9ccbd2)"></div>
      <div><span class="date">May 17, 2024</span><h4>News 1 Heading</h4><p>News 1 short sentence</p><div class="more">Read more ›</div></div>
    </div>
    <div class="news-item">
      <div class="thumb" role="img" aria-label="Photo of a truck on a coastal road" style="background:linear-gradient(135deg,#2f6f86,#86b9c6)"></div>
      <div><span class="date">May 10, 2024</span><h4>News 2 Heading</h4><p>News 2 short sentence</p><div class="more">Read more ›</div></div>
    </div>
  </div>

  <div class="clients">
    <h3 class="col-title">WHAT CLIENTS SAY</h3>
    <blockquote>"Lorem ipsum dolor sit amet, consectetur adipiscing elit, sed do eiusmod tempor incididunt ut labore et dolore magna aliqua. Ut enim ad minim veniam, quis nostrud exercitation ullamco laboris nisi ut aliquip ex ea commodo consequat."</blockquote>
    <div class="who">DRIVER LANE<span>INDEPENDENT TRUCKER</span></div>
    <div class="arrows">
      <svg viewBox="0 0 12 12"><rect width="12" height="12" fill="#3a4058"/><path d="M7 3L4 6l3 3" fill="none" stroke="#fff" stroke-width="1.2"/></svg>
      <svg viewBox="0 0 12 12"><rect width="12" height="12" fill="#4257c9"/><path d="M5 3l3 3-3 3" fill="none" stroke="#fff" stroke-width="1.2"/></svg>
    </div>
  </div>

  <div class="agent">
    <h3 class="col-title">TALK TO AN AGENT</h3>
    <div class="portrait" role="img" aria-label="Portrait photo of a customer service agent wearing a headset" style="background:radial-gradient(circle at 45% 40%,#d9c2ab,#8c7462)"></div>
    <p>Our licensed agents are ready to help you find the right coverage today.</p>
    <div class="phone"><svg width="9" height="9" viewBox="0 0 20 20"><path d="M5 3h3l1.5 4-2 1.3a9 9 0 004.2 4.2l1.3-2 4 1.5v3a1.5 1.5 0 01-1.6 1.5A14 14 0 013.5 4.6 1.5 1.5 0 015 3z" fill="#4257c9"/></svg>1-888-000-0000</div>
  </div>
</section>

<footer class="site-footer">
  <div>
    <h4>QUICK LINKS</h4><div class="line"></div>
    <ul><li>Link Number 1</li><li>Link Number 2</li><li>Link Number 3</li><li>Link Number 4</li><li>Link Number 5</li><li>Link Number 6</li></ul>
  </div>
  <div>
    <h4>FAQs</h4><div class="line"></div>
    <p>Frequently asked question number one goes here?</p>
    <p>Frequently asked question number two goes here?</p>
    <p>Frequently asked question number three goes here?</p>
  </div>
  <div>
    <h4>NEWSLETTER</h4><div class="line"></div>
    <p>Subscribe to our newsletter to get the latest trucking insurance news and updates.</p>
    <div class="field"><span>Enter your email</span><b><svg width="6" height="6" viewBox="0 0 6 6"><path d="M1 1l3 2-3 2" fill="none" stroke="#fff" stroke-width="1.2"/></svg></b></div>
  </div>
  <div>
    <h4>CONTACT US</h4><div class="line"></div>
    <p>Toll free: 1-888-000-0000<br>Phone: 000-000-0000<br>Fax: 000-000-0000</p>
    <p>1200 Harbor Road, Suite 4<br>Valley City, CA 00000<br>hello@roadlinecover.example</p>
  </div>
</footer>
<div class="footer-bar">© 2024 Roadline Cover. All rights reserved.</div>

</body>
</html>
```